Zielgruppe
Wir sind ein kleines Familienunternehmen mit 2-3 Friseurfilialen und Onlineshop im Naturfriseurbereich, arbeiten mit ökologischen, nachhaltigen und natürlichen Produkten und vertreiben unsere eigene Haarbürste. Wir betreiben mit Terra Lumis unsere eigene Marke in diesem Bereich. Erste Produkte, wie eine eigene Haarbürste sind bereits vorhanden und entstanden.
Für unsere erste Shampoo Serie suchen wir ein klares, cleanes und hochwertiges Design. Die 200ml Shampooflasche kommt komplett in weiß und besteh aus recyceltem Material. Es soll klar die ökologisch nachhaltige und etwas höherpreisige Marke kommuniziert werden. Dabei sehen wir vom Stil „weniger ist mehr“ als ganz klare Designvorgabe. Anbei auch ein Beispiel von Veralin, die das ganze sehr schön umgesetzt haben.
Die INCI sind noch nicht final. Es wäre schön, wenn hier ein Platzhalter eingefügt würde. Da eine der Hauptzielgruppen auch Österreicher sind, würden wir uns über ein kleines „Made in Austria“ auf der Vorderseite (evtl. ganz unten auf der Flasche) freuen.
Insgesamt sind es vier verschiedene Shampoos, die aus der gleichen Serie stammen. Es wäre schön, wenn man diese auch direkt unterscheiden könnte. Vielleicht durch ein grafisches Element, oder einfach nur durch die verschiedenen Namenserweiterungen. Hier die Aufstellung mit den Erweiterungen:
Es werden 4 verschiedene Shampoos, die Namen sind:
Change - Strapaziertes Haar
Care - Normales Haar
Sensitiv - Empfindliche Kopfhaut
Balancing - Fettiges Haar
Zielgruppe:
Weiblich, 30-60 Jahre, mittleres bis gehobenes Einkommen, nachhaltig, ökologisch, natürlich, legt Wert auf hochwertige Produkte und Dienstleistungen, achtet auf Konsum.
Aufgabenstellung
Die Landingpage zur Bürste ist hier erreichbar (Beispiel):
Vielleicht hilft das etwas um das Design und die Tonality aufzuschnappen: https://terra-lumis.de/blue-cedar-naturborstenbuerste/
Es wäre super, wenn das Design der Flasche ähnlich klar und strukturiert ist.
Die Shampoos sind komplett vegan und made in Austria. Die beiden Aspekte sollten in Design auch aufgegriffen werden. Da wir einen 4 farbigen Tamponade/Siebdruck auf der Flasche anwenden, stehen leider nicht so viele Farben zur Verfügung (3-4).
Link zur Flasche:
https://www.packorilo.com/de/kosmetik/tubora/tubora-forma/flasche-heavy-200ml-24-410-plastik
Des Weiteren kann sich noch am Terra Lumis Haarkonzept und unserem Dienstleistungsflyer orientiert werden.
Benefits:
-       Pflegt das Haar, hält es geschmeidig
- Bio Shampoo Konzentrat
-       Die Grundlage für gesunde Kopfhaut und schönes Haar*
-       Vermindert Spliss*
-       Hält die Haare natürlich geschmeidig
-       Regt die Durchblutung der Kopfhaut an
-       Verteilt Nährstoffe von der Wurzel bis in die Spitzen*
-       Verbessert das Kopfhautklima*
-       Für eine gut durchblutete und gesunde Kopfhaut mit glänzenden und
geschmeidigen Haaren*
-       Entfernt Schuppen und abgestorbene Hautpartikel
-       Verbessert natürlich die allgemeine Haarstruktur
-       Entwirrt langes und gelocktes Haar
-       Reinigt die Kopfhaut ohne Chemie*
-       Mehr Volumen im Haar
-       Mehr Stand im Haar durch Kräftigung der Haarbalkmuskulatur
-       Spart Shampoo und hilft Shampoo seltener und weniger zu nutzen
-       Nährstoffversorgung bis in die Haarspitzen
Inhaltsstoffe:
Care
Aloe Vera Direktsaft*, Decyl Glucoside, Coco Glucoside, Lauryl Glucoside, Hopfenextrakt*, Pentylene Glycol green, Meli..

```html
<!DOCTYPE html>
<html lang="de">
<head>
<meta charset="utf-8">
<title>Terra Lumis – Shampoo Etiketten</title>
<link href="https://fonts.googleapis.com/css2?family=Quicksand:wght@400;500&display=swap" rel="stylesheet">
<style>
  :root{
    --bg:#f3f3f3;
    --label:#ffffff;
    --peach:#fad7a0;
    --sage:#badaab;
    --ink:#111111;
    --brand:#2e3a8c;
  }
  *{margin:0;padding:0;box-sizing:border-box}
  html,body{width:1200px;height:1200px;overflow:hidden;background:var(--bg)}
  body{position:relative;font-family:"Quicksand",sans-serif;color:var(--ink)}
  .label{
    position:absolute;top:81px;width:461px;height:1046px;
    background:var(--label);overflow:hidden;
    box-shadow:0 0 12px rgba(0,0,0,.22);
  }
  .label--care{left:112px}
  .label--balancing{left:630px}
  .deco{position:absolute;left:0;top:0;width:461px;height:1046px}
  .brand{
    position:absolute;top:118px;left:148px;
    font-size:25px;font-weight:500;color:var(--brand);
    letter-spacing:.3px;line-height:28px;white-space:nowrap;
  }
  .product{position:absolute;left:0;width:100%;text-align:center}
  .product__name{font-weight:400;line-height:1}
  .label--care .product__name{font-size:90px}
  .label--balancing .product__name{font-size:56px}
  .product__type{font-size:26px;font-weight:400;letter-spacing:.5px;line-height:33px}
  .label--care .product__type{margin-top:10px}
  .label--balancing .product__type{margin-top:16px}
  .product__kind{font-size:15px;font-style:italic;margin-top:10px;letter-spacing:.3px}
  .label--care .product{top:331px}
  .label--balancing .product{top:372px}
  .illustration{
    position:absolute;border-radius:40px;
    background:linear-gradient(120deg,var(--peach) 0%,#f4e6c8 45%,var(--sage) 100%);
    opacity:.85;
  }
  .label--care .illustration{left:61px;top:615px;width:343px;height:430px}
  .label--balancing .illustration{left:22px;top:630px;width:423px;height:407px}
  .volume{position:absolute;left:5px;width:100%;text-align:center;font-size:15px;font-weight:500}
  .label--care .volume{top:980px}
  .label--balancing .volume{top:982px}
</style>
</head>
<body>

<section class="label label--care">
  <svg class="deco" viewBox="0 0 461 1046" aria-hidden="true">
    <path fill="var(--peach)" d="M48 0 H303 C310 40 300 70 260 82 C220 92 185 80 170 60 C150 36 140 42 110 50 C80 58 50 50 48 25 Z"/>
    <path fill="var(--sage)" d="M320 280 C350 270 375 295 368 330 C362 355 335 360 318 352 C305 345 318 335 315 325 C305 318 292 310 295 298 C298 288 310 283 320 280 Z"/>
  </svg>
  <p class="brand">Terra Lumis</p>
  <div class="product">
    <h1 class="product__name">Care</h1>
    <p class="product__type">Normales Haar</p>
    <p class="product__kind">Shampoo</p>
  </div>
  <div class="illustration" role="img" aria-label="Linienzeichnung einer Frau mit Blattzweig auf pfirsichfarbenen und grünen Flächen"></div>
  <p class="volume">250ml</p>
</section>

<section class="label label--balancing">
  <svg class="deco" viewBox="0 0 461 1046" aria-hidden="true">
    <path fill="var(--peach)" d="M75 0 H305 C320 25 300 50 250 60 C200 70 150 72 110 68 C75 64 58 45 63 25 C66 10 70 4 75 0 Z"/>
    <path fill="var(--peach)" d="M305 316 C330 310 365 335 372 360 C378 385 370 405 360 405 C345 400 340 385 320 375 C295 362 282 345 285 332 C288 322 295 318 305 316 Z"/>
  </svg>
  <p class="brand">Terra Lumis</p>
  <div class="product">
    <h1 class="product__name">Balancing</h1>
    <p class="product__type">Fettiges Haar</p>
    <p class="product__kind">Shampoo</p>
  </div>
  <div class="illustration" role="img" aria-label="Linienzeichnung eines Frauenkopfes mit Gräsern auf grünen und pfirsichfarbenen Flächen"></div>
  <p class="volume">250ml</p>
</section>

</body>
</html>
```